Nature photography website

We are looking for a template for a website where we will be posting nature photography (including landscape photography, macro, and timelapse), video, and music. Website name is "BloomVistaHub".

We have a logo (attached), which should be prominently featured, and the theme should revolve around those colours/designs. Logo can be slightly modified to suit the webpage if needed. Theme colours are purple, green, blue and yellow (purple/green being most prominent), while still looking natural, to keep with a nature theme. In regards to colours, artistic discretion is fine.

We are looking for something of a high standard, so if money offered is insufficient for your best work, please submit a template and inform us of the price required to meet that standard, and we will take it into consideration. Price offered is just a rough guide. We are, however, only willing to pay extra for something that is exceptional and exactly what we're looking for.

We are looking for something that is web2.0 featuring beautiful artistic designs, not using plain colour tones. Some texture is ok, so long as it fits with the theme. We are looking for a very natural look, featuring parts of nature (ie, leaves, trees, waterfalls, flowers, stars, etc., anything that can be considered natural and looks attractive on a webpage).
Updates

Project Deadline Extended
Reason: Need more designs.

Hey guys,

I've extended the deadline to give you all more time.

Heres an example of what where after:

http://www.trelvik.example/

Heres what we like:
* The site background is nature based. its blurry as to not take away from the foreground. 
* The content box has a textured background, not a plain color.
* Beautiful illustrations around the edges of the content boxes. (WE LOVE THESE) These fit nicely over the background. We like realistic illustrations rather than cartoon art.
* A nice footer at the bottom of the page.
 
I know this is extra work guys, but we will pay more for exceptional work. Just let us know what its worth.

Ill try to post some more examples as I find them.

THANKS FOR YOUR EFFORTS SO FAR.

Mort.

Industry/Entity Type

Landscape

Requirements
Must have
• Must be attractive and eye-catching (we are not looking for anything plain).

Must prominently feature our logo (attached).

Must feature natural images and designs (not stockphoto).

CSS style sheet, etc.
Nice to have
• Multiple designs and images, not busy to the eye, but very catching and attractive.
Should not have
• Do not want plain colour tones and themes.

```html
<!DOCTYPE html>
<html lang="en">
<head>
<meta charset="utf-8">
<title>BloomVistaHub – Nature Photography</title>
<link rel="stylesheet" href="https://fonts.googleapis.com/css2?family=PT+Sans:ital,wght@0,400;0,700;1,700&display=swap">
<style>
  :root {
    --bark-dark: #3a1f0e;
    --bark: #5a3418;
    --bark-light: #7a4a24;
    --wood: #6b3d1c;
    --wood-light: #9a6333;
    --leaf: #b5c234;
    --leaf-deep: #6f8c0c;
    --leaf-ink: #3f5210;
    --olive-title: #cdc53c;
    --foliage: #7fb83a;
    --foliage-deep: #3f7a1c;
    --white: #ffffff;
    --footer: #1f1f1f;
    --footer-text: #c9c9c9;
    --sky: #9fb6d4;
    --grass: #6fa32a;
  }
  html, body {
    margin: 0;
    padding: 0;
    width: 1145px;
    height: 1200px;
    overflow: hidden;
    background: var(--bark-dark);
    font-family: "PT Sans", Arial, sans-serif;
  }
  .page {
    position: relative;
    width: 1050px;
    height: 1100px;
    transform: scale(1.0905);
    transform-origin: 0 0;
    overflow: hidden;
    background:
      repeating-linear-gradient(115deg, rgba(0,0,0,.10) 0 2px, transparent 2px 5px),
      repeating-linear-gradient(65deg, rgba(255,255,255,.04) 0 1px, transparent 1px 4px),
      radial-gradient(ellipse at 50% 40%, var(--bark-light), var(--bark) 55%, var(--bark-dark));
  }
  .abs { position: absolute; }

  /* foliage framing the page edges */
  .foliage { position: absolute; }
  .foliage--top {
    left: 395px; top: 0; width: 290px; height: 125px;
    background: radial-gradient(ellipse 55% 75% at 50% 0, rgba(127,184,58,.95), rgba(90,150,40,.65) 55%, rgba(90,150,40,0) 100%);
  }
  .foliage--topright {
    left: 790px; top: 0; width: 260px; height: 340px;
    background:
      linear-gradient(90deg, rgba(63,122,28,0) 0, rgba(63,122,28,0) 75%, rgba(80,60,30,.7) 88%, rgba(63,122,28,.6) 100%),
      radial-gradient(ellipse 85% 70% at 85% 15%, rgba(127,184,58,.95), rgba(95,160,45,.7) 55%, rgba(95,160,45,0) 100%);
  }
  .foliage--left {
    left: 0; top: 130px; width: 130px; height: 170px;
    background: radial-gradient(ellipse 90% 55% at 0 45%, rgba(127,184,58,.9), rgba(95,160,45,.55) 55%, rgba(95,160,45,0) 100%);
  }
  .foliage--right {
    left: 985px; top: 590px; width: 65px; height: 390px;
    background: radial-gradient(ellipse 100% 60% at 100% 50%, rgba(110,180,60,.95), rgba(80,150,40,.6) 60%, rgba(80,150,40,0) 100%);
  }

  /* header */
  .brand { left: 52px; top: 50px; display: flex; align-items: center; gap: 10px;
    font-size: 30px; font-weight: 700; color: #8cbf2a; }
  .brand__dot { width: 26px; height: 26px; border-radius: 50%; background: #7a3fa0; }

  .wood-panel {
    background:
      repeating-linear-gradient(90deg, rgba(0,0,0,.12) 0 2px, transparent 2px 9px),
      linear-gradient(180deg, var(--wood-light), var(--wood) 50%, #4e2a12);
    box-shadow: 0 2px 6px rgba(0,0,0,.6), inset 0 1px 0 rgba(255,255,255,.2);
  }
  .search { left: 713px; top: 57px; width: 285px; height: 43px; border-radius: 3px; }
  .search__label { position: absolute; left: 12px; top: 12px; color: #f3e6d6; font-size: 14px; }
  .search__icon { position: absolute; right: 10px; top: 8px; }

  .nav { left: 48px; top: 134px; width: 955px; height: 53px; border-radius: 4px; }
  .nav__item { position: absolute; top: 17px; color: var(--white); font-size: 15px;
    text-transform: uppercase; text-shadow: 0 1px 2px rgba(0,0,0,.7); white-space: nowrap; }
  .nav__item--active { color: var(--olive-title); }
  .social { position: absolute; top: 13px; width: 26px; height: 26px; border-radius: 50%;
    background: var(--white); box-shadow: 0 1px 2px rgba(0,0,0,.5); }

  /* slider */
  .slider { left: 105px; top: 214px; width: 840px; height: 282px; background: #f6f6f6;
    box-shadow: 0 3px 10px rgba(0,0,0,.6); }
  .slider__photo { position: absolute; left: 21px; top: 14px; width: 798px; height: 254px;
    background: linear-gradient(180deg, #5e7fae 0%, var(--sky) 35%, #dfe7ef 62%, #8cbf3a 74%, #4f8a1c 100%); }
  .slider__caption { position: absolute; left: 73px; top: 100px; font-size: 25px; color: #1a1a1a; white-space: nowrap; }
  .slider__arrow { top: 340px; }
  .slider__accent { left: 866px; top: 408px; width: 112px; height: 114px;
    background: linear-gradient(160deg, rgba(150,205,80,.85), rgba(70,130,30,.85) 60%, rgba(50,50,50,.8)); }

  /* welcome */
  .section-title { margin: 0; font-size: 18px; font-weight: 400; color: var(--olive-title); text-transform: uppercase; letter-spacing: .3px; white-space: nowrap; }
  .welcome { left: 48px; top: 541px; width: 555px; }
  .welcome p { margin: 8px 0 0; font-size: 12.5px; line-height: 20px; color: var(--white); text-align: justify; }
  .btn { display: inline-block; background: var(--leaf-deep); color: var(--white); font-size: 13px;
    padding: 7px 10px; box-shadow: 0 1px 2px rgba(0,0,0,.4); white-space: nowrap; }
  .welcome__more { left: 525px; top: 697px; }

  /* galleries */
  .gallery { top: 751px; width: 184px; }
  .gallery__photo { margin-top: 8px; width: 180px; height: 112px; border: 2px solid #2e1a0c; }
  .gallery__label { margin-top: 8px; text-align: center; font-size: 11.5px; color: var(--olive-title); }
  .gallery__text { margin: 6px 2px 0; font-size: 10px; line-height: 14px; color: var(--white); text-align: justify; }
  .gallery__text b { color: var(--olive-title); }

  /* side boxes */
  .panel { left: 644px; width: 348px; background: var(--leaf); box-shadow: 0 2px 6px rgba(0,0,0,.5); }
  .panel .section-title { color: var(--leaf-ink); font-size: 19px; position: absolute; left: 14px; top: 15px; }
  .testimonials { top: 536px; height: 191px; }
  .testimonials__quote { position: absolute; left: 16px; top: 56px; width: 313px; margin: 0;
    font-size: 12.5px; line-height: 20px; color: var(--leaf-ink); text-align: justify; }
  .testimonials__mark { color: var(--leaf-deep); font-size: 26px; font-weight: 700; line-height: 10px; vertical-align: -6px; }
  .testimonials__name { position: absolute; left: 18px; top: 151px; font-size: 14px; font-weight: 700; font-style: italic; color: #1c1c1c; }
  .testimonials__btn { position: absolute; left: 270px; top: 148px; }

  .photographers { top: 747px; height: 192px; }
  .thumb { position: absolute; width: 68px; height: 56px; border: 2px solid var(--white); box-shadow: 0 1px 2px rgba(0,0,0,.35); }

  /* category band */
  .band { left: 0; top: 983px; width: 1050px; height: 57px; border-top: 2px solid var(--olive-title);
    background: linear-gradient(180deg, #4a2c14 0%, #5a3a1a 40%, #5f8e2a 80%, var(--grass) 100%); }
  .band__item { position: absolute; top: 21px; display: flex; align-items: center; gap: 7px;
    color: var(--white); font-size: 15px; text-transform: uppercase; text-shadow: 0 1px 2px rgba(0,0,0,.8); white-space: nowrap; }
  .band__dot { width: 15px; height: 15px; border-radius: 50%;
    background: radial-gradient(circle at 40% 40%, #5a6f9a, #111 65%); border: 1px solid #666; }

  /* footer */
  .footer { left: 0; top: 1040px; width: 1050px; height: 60px; background: var(--footer); }
  .footer__links { position: absolute; left: 44px; top: 21px; font-size: 12.5px; color: var(--footer-text); white-space: nowrap; }
  .footer__links span { margin: 0 9px; }
  .footer__copy { position: absolute; right: 42px; top: 21px; font-size: 12.5px; color: var(--footer-text); white-space: nowrap; }
</style>
</head>
<body>
<div class="page">
  <div class="foliage foliage--top" role="img" aria-label="Green leaves hanging from the top edge"></div>
  <div class="foliage foliage--topright" role="img" aria-label="Tree trunk and leafy branches at the top right"></div>
  <div class="foliage foliage--left" role="img" aria-label="Leafy branch reaching in from the left"></div>
  <div class="foliage foliage--right" role="img" aria-label="Fern fronds along the right edge"></div>

  <div class="abs brand"><span class="brand__dot"></span>BloomVistaHub</div>

  <div class="abs search wood-panel">
    <span class="search__label">Search</span>
    <svg class="search__icon" width="28" height="28" viewBox="0 0 28 28">
      <circle cx="11" cy="11" r="8" fill="none" stroke="#fff" stroke-width="3"/>
      <line x1="17" y1="17" x2="25" y2="25" stroke="#fff" stroke-width="4" stroke-linecap="round"/>
    </svg>
  </div>

  <nav class="abs nav wood-panel">
    <span class="nav__item nav__item--active" style="left:28px">Home</span>
    <span class="nav__item" style="left:137px">Blog</span>
    <span class="nav__item" style="left:243px">Photos</span>
    <span class="nav__item" style="left:369px">Tutorials</span>
    <span class="nav__item" style="left:517px">About</span>
    <span class="nav__item" style="left:633px">Contact</span>
    <span class="social" style="left:774px"></span>
    <span class="social" style="left:807px"></span>
    <span class="social" style="left:841px"></span>
    <span class="social" style="left:875px"></span>
    <span class="social" style="left:908px"></span>
  </nav>

  <div class="abs slider">
    <div class="slider__photo" role="img" aria-label="Lone tree on a green hill under a cloudy sky"></div>
    <div class="slider__caption">Exercitation ullamco laboris aliquip</div>
  </div>
  <svg class="abs slider__arrow" style="left:58px" width="22" height="32" viewBox="0 0 22 32">
    <polyline points="18,3 5,16 18,29" fill="none" stroke="#fff" stroke-width="5"/>
  </svg>
  <svg class="abs slider__arrow" style="left:968px" width="22" height="32" viewBox="0 0 22 32">
    <polyline points="4,3 17,16 4,29" fill="none" stroke="#fff" stroke-width="5"/>
  </svg>
  <div class="abs slider__accent" role="img" aria-label="Camera resting on a green leaf"></div>

  <section class="abs welcome">
    <h2 class="section-title">Welcome to our site</h2>
    <p>Perspiciatis unde omnis iste natus error sit voluptatem accusantium doloremque laudantium, totam rem aperiam, eaque ipsa quae ab illo inventore veritatis et quasi architecto beatae vitae dicta sunt explicabo. Nemo enim ipsam voluptatem quia voluptas sit aspernatur aut odit aut fugit, sed quia consequuntur magni dolores eos qui ratione voluptatem sequi nesciunt. Neque porro quisquam est, qui dolorem ipsum quia dolor sit amet, consectetur, adipisci velit, sed quia non numquam eius modi tempora incidunt ut labore et dolore magnam aliquam quaerat voluptatem.</p>
  </section>
  <span class="abs btn welcome__more">View more</span>

  <article class="abs gallery" style="left:48px">
    <h3 class="section-title">Trees</h3>
    <div class="gallery__photo" role="img" aria-label="Path through a green forest" style="background:linear-gradient(180deg,#a8d84a,#3f7a1c 60%,#2a3a14)"></div>
    <div class="gallery__label">DENOUNCE</div>
    <p class="gallery__text">Perspiciatis unde omnis iste natus error sit voluptatem accusantium doloremque laudantium <b>more...</b></p>
  </article>
  <article class="abs gallery" style="left:244px">
    <h3 class="section-title">Leaves</h3>
    <div class="gallery__photo" role="img" aria-label="Autumn maple leaves" style="background:linear-gradient(135deg,#f2c21e,#e07a1a 55%,#c0301a)"></div>
    <div class="gallery__label">DENOUNCE</div>
    <p class="gallery__text">Perspiciatis unde omnis iste natus error sit voluptatem accusantium doloremque laudantium <b>more...</b></p>
  </article>
  <article class="abs gallery" style="left:440px">
    <h3 class="section-title">Flowers</h3>
    <div class="gallery__photo" role="img" aria-label="Bouquet of pink and white roses" style="background:radial-gradient(circle at 45% 55%,#f6eee6,#e89ab8 45%,#b45a88)"></div>
    <div class="gallery__label">DENOUNCE</div>
    <p class="gallery__text">Perspiciatis unde omnis iste natus error sit voluptatem accusantium doloremque laudantium <b>more...</b></p>
  </article>

  <section class="abs panel testimonials">
    <h2 class="section-title">Testimonials</h2>
    <p class="testimonials__quote"><span class="testimonials__mark">&ldquo;</span> Enim ad minim veniam, quis nostrud exercitation ullamco laboris nisi ut aliquip ex ea commodo consequat. Duis aute irure dolor in reprehenderit in voluptate velit esse cillum dolore eu fugiat nulla pariatur. <span class="testimonials__mark">&rdquo;</span></p>
    <span class="testimonials__name">Necessitatibus</span>
    <span class="btn testimonials__btn">View All</span>
  </section>

  <section class="abs panel photographers">
    <h2 class="section-title">Photographers</h2>
    <div class="thumb" role="img" aria-label="Photographer with camera" style="left:12px;top:45px;background:linear-gradient(#eee,#8a6a4a)"></div>
    <div class="thumb" role="img" aria-label="Figure against a bright misty sky" style="left:93px;top:45px;background:linear-gradient(#dfe4ee,#6f7a8e)"></div>
    <div class="thumb" role="img" aria-label="Black and white photographer portrait" style="left:174px;top:45px;background:linear-gradient(#ddd,#555)"></div>
    <div class="thumb" role="img" aria-label="Photographer on dark background" style="left:255px;top:45px;background:linear-gradient(#333,#111)"></div>
    <div class="thumb" role="img" aria-label="Silhouette at sunset with camera" style="left:12px;top:116px;background:linear-gradient(#e8902a,#2a1a10)"></div>
    <div class="thumb" role="img" aria-label="Camera on tripod outdoors" style="left:93px;top:116px;background:linear-gradient(#c8c2a4,#8a7a4a)"></div>
    <div class="thumb" role="img" aria-label="Camera lens on white" style="left:174px;top:116px;background:linear-gradient(#fff,#bbb)"></div>
    <div class="thumb" role="img" aria-label="Photographer kneeling outdoors" style="left:255px;top:116px;background:linear-gradient(#cfe0c4,#5a7a6a)"></div>
  </section>

  <nav class="abs band" aria-label="Categories">
    <span class="band__item" style="left:60px"><span class="band__dot"></span>Leaves</span>
    <span class="band__item" style="left:169px"><span class="band__dot"></span>Trees</span>
    <span class="band__item" style="left:269px"><span class="band__dot"></span>Waterfalls</span>
    <span class="band__item" style="left:420px"><span class="band__dot"></span>Flowers</span>
    <span class="band__item" style="left:541px"><span class="band__dot"></span>Stars</span>
    <span class="band__item" style="left:642px"><span class="band__dot"></span>Animals</span>
    <span class="band__item" style="left:762px"><span class="band__dot"></span>Birds</span>
    <span class="band__item" style="left:862px"><span class="band__dot"></span>Landscape</span>
  </nav>

  <footer class="abs footer">
    <div class="footer__links">Home<span>|</span>Blog<span>|</span>Photos<span>|</span>Tutorials<span>|</span>About<span>|</span>Photographers<span>|</span>contact<span>|</span>Sitemap</div>
    <div class="footer__copy">Copyright &copy; 2011 www.BloomVistaHub.com &nbsp;&nbsp; All rights reserved</div>
  </footer>
</div>
</body>
</html>
```